"Rise. Shift. Thrive." Empowerment Book Cover

Hello, I need a hot, trendy, and contemporary book cover designed for my first book called "Rise. Shift. Thrive. -- 360 Bold Momentum Notes to Guide Anyone to Rise, Shift, and Thrive in Their Career & Daily Dreams."
This is my first book and I am really wanting to launch my brand with it... it would be awesome to match the inside/outside branding of the book. So we can either create the book cover to match the book guts, or update the book guts to match the cover.
Lastly, I just got a professional photoshoot done last week so we can use one of those images, or we can go with a different idea/style for the cover. The body of the book is attached. All questions welcomed, happy designing!
Target Market(s)
Gen Z, Millennials and Gen X.
Industry/Entity Type
Personal Development.
Requirements
Must have
- It must stand out and be different from other typical book covers.
Nice to have
- Success, Inspiration, Motivation, Mindset, Growth.
Should not have
- Clipart, stock art, stock look and feel.

```html
<!DOCTYPE html>
<html lang="en">
<head>
<meta charset="utf-8">
<title>Rise. Shift. Thrive. Book Cover</title>
<link href="https://fonts.googleapis.com/css2?family=Anton&family=Poppins:ital,wght@0,300;0,400;0,500;1,500&display=swap" rel="stylesheet">
<style>
  :root {
    --bg: #dfe4e3;
    --ink: #000000;
    --paper: #f4f4f4;
    --green: #14f58a;
    --text-light: #f2f2f2;
    --tone-light: #c9c9c9;
    --tone-mid: #6a6a6a;
    --tone-dark: #2b2b2b;
  }
  html, body {
    margin: 0;
    padding: 0;
    width: 1200px;
    height: 675px;
    overflow: hidden;
    background: var(--bg);
  }
  .spread {
    position: absolute;
    left: 182px;
    top: 37px;
    width: 836px;
    height: 600px;
    display: flex;
    box-shadow: 0 10px 30px rgba(0,0,0,0.18);
  }
  .back-cover, .spine, .front-cover {
    position: relative;
    height: 600px;
    background: var(--ink);
    color: var(--text-light);
    overflow: hidden;
  }
  .back-cover { width: 400px; }
  .spine { width: 36px; border-left: 1px solid #1a1a1a; border-right: 1px solid #1a1a1a; box-sizing: border-box; }
  .front-cover { width: 400px; }

  /* back cover */
  .back-subtitle {
    position: absolute; left: 30px; right: 30px; top: 52px;
    font-family: "Poppins", sans-serif; font-weight: 500; font-size: 11px;
    line-height: 1.35; text-align: center; margin: 0;
  }
  .back-title {
    position: absolute; left: 130px; top: 100px; margin: 0;
    font-family: "Anton", sans-serif; font-weight: 400; font-size: 38px;
    line-height: 1.02; color: var(--green); letter-spacing: -0.5px;
  }
  .back-blurb {
    position: absolute; left: 30px; right: 30px; top: 262px;
    font-family: "Poppins", sans-serif; font-size: 9.5px; line-height: 1.75;
  }
  .back-blurb p { margin: 0 0 18px; text-align: justify; text-align-last: center; }

  /* spine */
  .spine-title {
    position: absolute; left: 50%; top: 50%;
    transform: translate(-50%, -50%) rotate(90deg);
    white-space: nowrap;
    font-family: "Anton", sans-serif; font-size: 24px; color: var(--green);
    letter-spacing: 1px;
  }

  /* front cover */
  .portrait-area {
    position: absolute; left: 0; top: 0; width: 330px; height: 600px;
    background:
      radial-gradient(ellipse 70px 85px at 120px 120px, rgba(150,150,150,0.9) 0%, rgba(110,110,110,0.6) 55%, rgba(0,0,0,0) 100%),
      radial-gradient(ellipse 170px 330px at 130px 420px, rgba(58,58,58,0.95) 0%, rgba(40,40,40,0.7) 60%, rgba(0,0,0,0) 100%),
      linear-gradient(90deg, var(--paper) 0%, var(--tone-light) 7%, var(--tone-mid) 18%, var(--tone-dark) 38%, #141414 70%, var(--ink) 100%);
  }
  .front-subtitle {
    position: absolute; left: 210px; width: 170px; top: 48px; margin: 0;
    font-family: "Poppins", sans-serif; font-style: italic; font-weight: 500;
    font-size: 12.5px; line-height: 1.3; text-align: center;
  }
  .front-title {
    position: absolute; left: 30px; top: 178px; margin: 0;
    font-family: "Anton", sans-serif; font-weight: 400; font-size: 104px;
    line-height: 0.98; color: var(--green); letter-spacing: -2px;
  }
  .front-title span { display: block; }
  .author-name {
    position: absolute; left: 0; right: 60px; top: 512px; margin: 0;
    font-family: "Poppins", sans-serif; font-weight: 300; font-size: 22px;
    letter-spacing: 1.5px; text-align: center; text-transform: uppercase;
  }
</style>
</head>
<body>
  <div class="spread">
    <section class="back-cover">
      <p class="back-subtitle">360 Bold Momentum Notes to Guide Anyone to Rise, Shift, and Thrive in Their Career &amp; Daily Dreams.</p>
      <h2 class="back-title">Rise.<br>Shift.<br>Thrive.</h2>
      <div class="back-blurb">
        <p>Small moves add up. This book gives you one short note for every day, each built to help you rise from where you stand, shift the habits that hold you back, and thrive at work and at home. Read one each morning, act on it before noon, and watch momentum build week after week.</p>
        <p>No theory, no fluff. Just clear prompts drawn from real wins and real setbacks, written for people who want progress they can feel. Keep it on your desk, mark the pages that hit hardest, and come back whenever you need a push toward the next bold step in your career and your daily dreams.</p>
      </div>
    </section>
    <section class="spine">
      <div class="spine-title">Rise.&nbsp; Shift.&nbsp; Thrive.</div>
    </section>
    <section class="front-cover">
      <div class="portrait-area" role="img" aria-label="Black and white portrait of the author in a dark suit, smiling, set against a background fading from white on the left to black"></div>
      <p class="front-subtitle">360 Bold Momentum Notes to Guide Anyone to Rise, Shift, and Thrive in Their Career &amp; Daily Dreams</p>
      <h1 class="front-title"><span>Rise.</span><span>Shift.</span><span>Thrive.</span></h1>
      <p class="author-name">Karan Mehta</p>
    </section>
  </div>
</body>
</html>
```